website design for Company KMV

Our company name KMV(the civic canvas limited), need design a website. It is a website that focuses on promoting art design in the world.
We will provide the existing logo design, the new website and logo should be matched to each other. The website has to include pages "Home" "Contact" "Service" and So on at least 6-8 pages. The site is mainly for publicity and promotion. We will have an existing domain and hosting.
Updates

We prefer the original design, thanks.

Target Market(s)

large public art

Industry/Entity Type

Architecture and design, large public art and sculpture manufacturer

Coding

Coded - Design and coding required

Number of Pages Required

5+ page

Requirements
Must have
• 1. the overall color has to match our logo color 2. Do not need to do any change on our logo including the color 3. Here is a similar style of the home page we like, it can be similar but must not same. Pls check the below link. https://www.darveno.example/en-us/

```html
<!DOCTYPE html>
<html lang="en">
<head>
<meta charset="utf-8">
<title>KMV – The Civic Canvas</title>
<link href="https://fonts.googleapis.com/css2?family=Barlow:wght@300;400;600;700&family=Arimo:wght@400;700&family=Montserrat:wght@500;600;700&display=swap" rel="stylesheet">
<style>
:root{
  --ink:#1c1c1c;
  --dark:#262626;
  --charcoal:#2f2f2f;
  --white:#ffffff;
  --paper:#f2f2f2;
  --grey:#8a8a8a;
  --text:#555555;
  --teal:#1f3b45;
  --blog-accent:#2a1414;
}
*{box-sizing:border-box;margin:0;padding:0}
html,body{width:1200px;height:4332px;overflow:hidden}
body{position:relative;background:var(--white);font-family:"Arimo",Arial,sans-serif;color:var(--text)}
.section{position:absolute;left:0;width:1200px;overflow:hidden}
.abs{position:absolute}
.photo{position:absolute}
.h-light{font-family:"Barlow",sans-serif;font-weight:300}
.h-bold{font-family:"Barlow",sans-serif;font-weight:700}
.btn{position:absolute;display:flex;align-items:center;justify-content:center;font-family:"Montserrat",sans-serif;font-weight:600;font-size:13px;letter-spacing:2px;text-transform:uppercase}
.rule{position:absolute;height:3px;background:var(--ink)}

/* hero */
.hero{top:0;height:657px}
.hero .photo{inset:0;background:
  radial-gradient(ellipse 420px 300px at 600px 470px,rgba(150,160,170,.45),rgba(150,160,170,0) 70%),
  linear-gradient(180deg,#2f3134 0%,#45474b 22%,#5b5552 40%,#7a5f48 58%,#5a4636 76%,#262422 100%)}
.brand{position:absolute;left:106px;top:18px;display:flex;align-items:center;gap:14px;color:var(--white);font-family:"Barlow",sans-serif;font-weight:400}
.brand-name{font-size:40px;letter-spacing:2px}
.brand-sub{font-size:20px;letter-spacing:3px;line-height:20px}
.nav{position:absolute;top:30px;left:454px;font-family:"Arimo",sans-serif;font-size:13px;color:var(--white)}
.nav a{color:var(--white);text-decoration:none;position:absolute;white-space:nowrap}
.nav .active{font-weight:700}
.nav .active::after{content:"";position:absolute;left:0;right:0;top:24px;height:1px;background:var(--white)}
.hero-title{position:absolute;top:236px;width:100%;text-align:center;color:var(--white);font-family:"Barlow",sans-serif;font-weight:400;font-size:84px;letter-spacing:2px}
.hero-sub{position:absolute;top:338px;width:100%;text-align:center;color:var(--white);font-family:"Barlow",sans-serif;font-weight:300;font-size:29px;letter-spacing:1px}

/* about */
.about{top:657px;height:654px;background:var(--white)}
.about .panel{left:0;top:0;width:386px;height:654px;background:var(--dark)}
.about-title{left:644px;top:178px;font-size:44px;color:var(--ink)}
.about-text{left:652px;top:264px;width:440px;font-size:14.5px;line-height:27px;color:var(--text)}
.about-text p+p{margin-top:10px}
.about .btn{left:650px;top:443px;width:178px;height:48px;border:2px solid var(--teal);border-radius:24px;color:var(--ink)}

/* services */
.services{top:1311px;height:542px;background:linear-gradient(180deg,#f4f4f4,#e6e6e6)}
.sec-title{position:absolute;width:100%;text-align:center;font-size:42px;color:var(--ink)}
.card{position:absolute;top:173px;width:395px;height:280px}
.card .cap{position:absolute;left:0;right:0;top:210px;text-align:center;color:var(--white);font-family:"Barlow",sans-serif;font-weight:700;font-size:20px;line-height:25px}
.card .cap::after{content:"";display:block;width:34px;height:2px;background:var(--white);margin:10px auto 0}

/* design */
.design{top:1853px;height:526px}
.design .photo{inset:0;background:
  radial-gradient(ellipse 260px 200px at 260px 160px,rgba(140,110,60,.55),rgba(140,110,60,0) 70%),
  radial-gradient(ellipse 200px 180px at 1030px 260px,rgba(120,90,50,.5),rgba(120,90,50,0) 70%),
  radial-gradient(ellipse 160px 300px at 600px 360px,rgba(30,30,30,.6),rgba(30,30,30,0) 70%),
  linear-gradient(180deg,#7e7d79,#5f5e5a 50%,#8f8d88)}
.design .sec-title{top:136px;color:var(--white)}
.design-text{position:absolute;top:222px;left:262px;width:676px;text-align:center;color:var(--white);font-size:15.5px;line-height:24px}
.design .btn{left:511px;top:319px;width:178px;height:46px;border:2px solid var(--white);border-radius:23px;color:var(--white)}

/* artists */
.artists{top:2379px;height:497px;background:var(--white)}
.eyebrow{left:129px;top:113px;font-size:15px;letter-spacing:2px;color:var(--text)}
.artists-title{left:129px;top:137px;font-size:40px;color:var(--ink)}
.artists-text{left:129px;top:217px;width:420px;font-size:14.5px;line-height:27px}
.artists .btn{left:129px;top:351px;width:180px;height:49px;border:2px solid var(--grey);color:var(--ink)}

/* blogs */
.blogs{top:2876px;height:602px;background:var(--paper)}
.post{position:absolute;top:146px;width:317px;height:348px;background:var(--white)}
.post .photo{left:0;top:0;width:317px;height:207px}
.date{position:absolute;left:0;top:187px;width:110px;height:20px;background:var(--charcoal);color:var(--white);font-family:"Montserrat",sans-serif;font-weight:600;font-size:10.5px;line-height:20px;padding-left:22px}
.post h3{position:absolute;left:32px;top:230px;width:270px;font-weight:700;font-size:14.5px;line-height:19px;color:var(--ink)}
.post p{position:absolute;left:32px;top:277px;font-size:11px;color:var(--grey)}
.post a{position:absolute;left:32px;top:302px;font-family:"Montserrat",sans-serif;font-weight:700;font-size:10.5px;color:var(--ink);text-decoration:none}

/* contact */
.contact{top:3478px;height:453px}
.contact .photo{inset:0;background:
  radial-gradient(ellipse 500px 260px at 600px 250px,rgba(80,80,80,.55),rgba(80,80,80,0) 70%),
  linear-gradient(135deg,#161616,#3a3a3a 45%,#1c1c1c 70%,#2c2c2c)}
.contact .sec-title{top:116px;color:var(--white)}
.contact-text{position:absolute;top:197px;left:270px;width:660px;text-align:center;color:#cfcfcf;font-size:14.5px;line-height:29px}
.contact .btn{left:511px;top:272px;width:178px;height:46px;border:2px solid #bdbdbd;color:var(--white)}

/* footer */
.footer{top:3931px;height:401px;background:var(--white)}
.fcol{position:absolute;top:78px}
.fcol h4{font-family:"Montserrat",sans-serif;font-weight:700;font-size:17px;letter-spacing:1px;color:var(--ink)}
.fcol h4::after{content:"";display:block;width:30px;height:2px;background:var(--ink);margin-top:10px}
.fcol ul{list-style:none;margin-top:18px}
.fcol li{font-size:12px;color:var(--ink);height:27px}
.info{display:flex;gap:16px;margin-top:20px}
.info small{display:block;font-size:11.5px;color:var(--text)}
.info b{display:block;font-weight:400;font-size:15px;color:var(--ink)}
.social li{display:flex;align-items:center;gap:12px;height:39px}
.social .dot{width:24px;height:24px;border-radius:50%;background:var(--ink)}
.foot-line{left:0;top:322px;width:1200px;height:1px;background:#dcdcdc}
.copy{position:absolute;top:346px;width:100%;text-align:center;font-size:12px;color:var(--text)}
</style>
</head>
<body>

<header class="section hero">
  <div class="photo" role="img" aria-label="Dusk view of a classical palace courtyard with a glass pyramid in front"></div>
  <div class="brand">
    <span class="brand-name">KMV</span>
    <span class="brand-sub">THE CIVIC<br>CANVAS</span>
  </div>
  <nav class="nav">
    <a class="active" style="left:0">ABOUT US</a>
    <a style="left:119px">SERVICES</a>
    <a style="left:232px">ARTISTS</a>
    <a style="left:337px">PUBLIC ART</a>
    <a style="left:464px">BLOGS</a>
    <a style="left:559px">CONTACT</a>
  </nav>
  <h1 class="hero-title">THE CIVIC CANVAS</h1>
  <p class="hero-sub">ART &amp; DESIGN AROUND THE WORLD</p>
  <svg class="abs" style="left:587px;top:584px" width="26" height="46" viewBox="0 0 26 46" aria-hidden="true">
    <rect x="6" y="1" width="14" height="24" rx="7" fill="none" stroke="#fff" stroke-width="1.5"/>
    <line x1="13" y1="6" x2="13" y2="11" stroke="#fff" stroke-width="1.5"/>
    <path d="M8 31l5 5 5-5M8 38l5 5 5-5" fill="none" stroke="#fff" stroke-width="1.5"/>
  </svg>
</header>

<section class="section about">
  <div class="abs panel"></div>
  <svg class="abs" style="left:700px;top:0" width="500" height="654" aria-hidden="true">
    <polygon points="500,120 500,220 180,500 90,500" fill="#f3f3f3"/>
  </svg>
  <div class="abs" style="left:119px;top:123px;width:242px;height:225px;border-top:3px solid #bfbfbf;border-left:3px solid #bfbfbf"></div>
  <svg class="abs" style="left:463px;top:440px" width="125" height="125" aria-hidden="true">
    <defs><pattern id="dots" width="6" height="6" patternUnits="userSpaceOnUse"><circle cx="2" cy="2" r="1.1" fill="#555"/></pattern></defs>
    <rect width="125" height="125" fill="url(#dots)"/>
  </svg>
  <div class="photo" style="left:133px;top:134px;width:432px;height:400px;background:
    radial-gradient(ellipse 160px 130px at 240px 250px,rgba(196,170,130,.8),rgba(196,170,130,0) 70%),
    linear-gradient(160deg,#c7d0d8,#b8b2a6 40%,#9a8b76 70%,#6d6258)" role="img" aria-label="Stone lion sculpture inside a glass-roofed museum court"></div>
  <h2 class="abs about-title"><span class="h-light">THE </span><span class="h-bold" style="font-weight:600">CIVIC CANVAS</span></h2>
  <div class="abs about-text">
    <p>Lorem ipsum dolor sit amet, consectetur adipiscing elit, sed do eiusmod tempor incididunt ut labore et dolore magna aliqua. Ut enim ad minim veniam, quis nostrud</p>
    <p>Axercitation ullamco laboris nisi ut aliquip ex ea commodo consequat. Duis aute irure dolor in reprehenderit.</p>
  </div>
  <a class="btn">Learn More</a>
</section>

<section class="section services">
  <svg class="abs" style="left:0;top:0" width="1200" height="542" aria-hidden="true">
    <path d="M700 0 Q950 60 1200 20 L1200 120 Q950 160 760 0Z" fill="#ffffff" opacity=".6"/>
    <path d="M0 470 Q400 500 800 542 L0 542Z" fill="#ffffff" opacity=".55"/>
  </svg>
  <h2 class="sec-title" style="top:56px"><span class="h-light">OUR </span><span class="h-bold">SERVICES</span></h2>
  <div class="rule" style="left:568px;top:110px;width:64px"></div>
  <div class="card" style="left:0">
    <div class="photo" style="inset:0;background:linear-gradient(125deg,#5a5a5a,#2a2a2a 45%,#1e1e1e 65%,#4d4d4d)" role="img" aria-label="Angular modern building facade in black and white"></div>
    <div class="cap">LOREM IPSUM DOLOR<br>CONSECTETUR</div>
  </div>
  <div class="card" style="left:402px">
    <div class="photo" style="inset:0;background:linear-gradient(180deg,#5c5c5c,#8a8a8a 50%,#b0b0b0 70%,#6e6e6e)" role="img" aria-label="White modernist building blocks in black and white"></div>
    <div class="cap">LOREM IPSUM DOLOR<br>CONSECTETUR</div>
  </div>
  <div class="card" style="left:805px">
    <div class="photo" style="inset:0;background:
      radial-gradient(ellipse 110px 140px at 220px 110px,rgba(170,170,170,.6),rgba(170,170,170,0) 70%),
      linear-gradient(180deg,#555,#3a3a3a)" role="img" aria-label="Winged classical statue in a stone hall, black and white"></div>
    <div class="cap">LOREM IPSUM DOLOR<br>CONSECTETUR</div>
  </div>
</section>

<section class="section design">
  <div class="photo" role="img" aria-label="Gallery room with framed paintings and a bronze statue on a round plinth"></div>
  <h2 class="sec-title"><span class="h-light">OUR </span><span class="h-bold">DESIGN &amp; ART</span></h2>
  <p class="design-text">Lorem ipsum dolor sit amet, consectetur adipiscing elit, sed do eiusmod tempor incididunt ut labore et dolore magna aliqua. Ut enim ad minim veniam.</p>
  <a class="btn">Learn More</a>
</section>

<section class="section artists">
  <p class="abs eyebrow">OUR ARTISTS</p>
  <h2 class="abs artists-title"><span class="h-light">MEET </span><span class="h-bold">ARTISTS</span></h2>
  <p class="abs artists-text">Lorem ipsum dolor sit amet, consectetur adipiscing elit, sed do eiusmod tempor incididunt ut labore et dolore magna aliqua. Ut enim ad minim veniam, quis nostrud Axercitation ullamco laboris nisi ut aliquip ex ea commodo</p>
  <a class="btn">Learn More</a>
  <div class="photo" style="left:600px;top:0;width:600px;height:497px;background:
    radial-gradient(ellipse 120px 200px at 300px 300px,rgba(50,45,40,.55),rgba(50,45,40,0) 70%),
    linear-gradient(160deg,#5a79ad,#9aaccb 25%,#d2c3a4 50%,#b39f80 75%,#6e6150)" role="img" aria-label="Bronze armillary sphere sculpture in front of a skyscraper"></div>
</section>

<section class="section blogs">
  <h2 class="sec-title" style="top:54px"><span class="h-light">LATEST </span><span class="h-bold" style="color:var(--blog-accent)">BLOGS</span></h2>
  <div class="rule" style="left:568px;top:108px;width:64px;background:var(--blog-accent)"></div>
  <article class="post" style="left:109px">
    <div class="photo" style="background:linear-gradient(160deg,#6f8aa4,#8a5a3c 45%,#6b3f28 65%,#3a3a3a)" role="img" aria-label="Honeycomb staircase structure of copper steel"></div>
    <span class="date">DEC 25, 2021</span>
    <h3>Lorem ipsum dolor sit met consect-etur adipiscing elit</h3>
    <p>Excepteur sint occaecat cupidatat non proident</p>
    <a>LEARN MORE</a>
  </article>
  <article class="post" style="left:447px">
    <div class="photo" style="background:linear-gradient(180deg,#e2e2e2,#9a9a9a 45%,#4a4a4a 60%,#c2c2c2)" role="img" aria-label="Black and white gallery interior with modern seating"></div>
    <span class="date">DEC 25, 2021</span>
    <h3>Lorem ipsum dolor sit met consect-etur adipiscing elit</h3>
    <p>Excepteur sint occaecat cupidatat non proident</p>
    <a>LEARN MORE</a>
  </article>
  <article class="post" style="left:785px">
    <div class="photo" style="background:linear-gradient(180deg,#efece6,#d6cfbf 45%,#b8ad98 65%,#4e5e50)" role="img" aria-label="Skylit gallery with colourful paintings and green benches"></div>
    <span class="date">DEC 25, 2021</span>
    <h3>Lorem ipsum dolor sit met consect-etur adipiscing elit</h3>
    <p>Excepteur sint occaecat cupidatat non proident</p>
    <a>LEARN MORE</a>
  </article>
</section>

<section class="section contact">
  <div class="photo" role="img" aria-label="Dark angular steel and glass architecture"></div>
  <h2 class="sec-title"><span class="h-light">CONTACT </span><span class="h-bold" style="font-weight:600">KMV</span></h2>
  <div class="rule" style="left:570px;top:172px;width:60px;background:#fff;height:2px"></div>
  <p class="contact-text">Lorem ipsum dolor sit amet, consectetur adipiscing elit, sed do eiusmod tempor incididunt ut labore et dolore magna aliqua. Ut enim ad minim veniam quis nostrud.</p>
  <a class="btn">Get in Touch</a>
</section>

<footer class="section footer">
  <div class="fcol" style="left:118px">
    <h4>COMPANY</h4>
    <ul><li>About Us</li><li>Our Services</li><li>Art &amp; Design</li><li>Artists</li></ul>
  </div>
  <div class="fcol" style="left:344px">
    <h4>RESOURCES</h4>
    <ul><li>Blogs</li><li>Privacy Policy</li><li>Legal</li><li>Contact Us</li></ul>
  </div>
  <div class="fcol" style="left:586px">
    <h4>CONTACT US</h4>
    <div class="info">
      <svg width="30" height="30" viewBox="0 0 24 24" aria-hidden="true"><path d="M6.6 2.5l3 3-2 2.3c1.2 2.6 3.3 4.7 5.9 5.9l2.3-2 3 3-2.2 2.8C10 17.3 3.6 10.9 3.8 4.7z" fill="none" stroke="#555" stroke-width="1.3"/></svg>
      <div><small>Phone Number</small><b>(+100) 555 0142</b></div>
    </div>
    <div class="info" style="margin-top:22px">
      <svg width="30" height="30" viewBox="0 0 24 24" aria-hidden="true"><rect x="2.5" y="5.5" width="19" height="13" fill="none" stroke="#555" stroke-width="1.3"/><path d="M2.5 5.5l9.5 8 9.5-8M2.5 18.5l7-6.5M21.5 18.5l-7-6.5" fill="none" stroke="#555" stroke-width="1.3"/></svg>
      <div><small>Email address</small><b>civiccanvas@info.example</b></div>
    </div>
  </div>
  <div class="fcol" style="left:911px">
    <h4>GET IN TOUCH</h4>
    <ul class="social" style="margin-top:10px">
      <li><span class="dot"></span>Socialbook</li>
      <li><span class="dot"></span>Chirper</li>
      <li><span class="dot"></span>WorkLink</li>
    </ul>
  </div>
  <div class="abs foot-line"></div>
  <p class="copy">© 2021 Company Name | All Rights Reserved</p>
</footer>

</body>
</html>
```